Thornwell Building Company - advertisement poster

I am looking to print some canvas signs to advertise my general contracting company, Thornwell Building Company. The sign will measure 6' long x 3' high so the size should match that ratio. I already have a logo icon, which is the Letter 'A' and some trees that I would like to incorporate, see attached. I would also like the to have the following information listed:
1) phone number: 472-318-6095
2) email: thornwellbuildingcompany@mailvistra.net
3) website: thornwellbuildingcompany.com
4) Lic#5386204
5) I want to use this text: "BUILD WITH THE T-CREW!"

The ad should be relatively simple and clean. Black and Green are my company colors. I am open to creative ideas!

Target Market(s)

People looking to renovate their homes

Industry/Entity Type

Construction

Colors
59FF00
82FF00
B8FF75
E3FFCB
F4FFEA

Requirements
Must have
• Must have my company logo
Should not have
• No photos or complex graphics

```html
<!DOCTYPE html>
<html lang="en">
<head>
<meta charset="utf-8">
<title>Thornwell Building Company – Sign</title>
<link rel="stylesheet" href="https://fonts.googleapis.com/css2?family=Montserrat:ital,wght@0,400;0,700;0,800;1,900&display=swap">
<style>
  :root {
    --stage: #8e8e8e;
    --sign: #ffffff;
    --black: #000000;
    --green: #62f000;
    --navy: #000099;
    --ink: #111111;
  }
  * { margin: 0; padding: 0; box-sizing: border-box; }
  html, body { width: 1200px; height: 1200px; overflow: hidden; background: var(--stage); }
  body { position: relative; font-family: "Montserrat", Arial, sans-serif; }

  .sign {
    position: absolute; left: 32px; top: 316px;
    width: 1135px; height: 567px;
    background: var(--sign); overflow: hidden;
  }
  .sign-corners { position: absolute; inset: 0; width: 100%; height: 100%; }

  .brand {
    position: absolute; left: 32px; top: 28px; width: 220px;
    text-align: center; color: #fff; font-weight: 700; line-height: 1;
  }
  .brand-mark { display: block; width: 34px; height: 34px; margin: 0 auto 14px; background: var(--green); }
  .brand-name { display: block; font-size: 31px; letter-spacing: 0.5px; }
  .brand-sub { display: block; font-size: 12.5px; letter-spacing: 3.4px; margin-top: 8px; }

  .headline {
    position: absolute; left: 444px; top: 40px;
    font-size: 158px; font-weight: 900; font-style: italic;
    color: var(--navy); letter-spacing: -6px; line-height: 1;
  }
  .tagline {
    position: absolute; left: 444px; top: 204px; height: 68px;
    display: flex; align-items: center; white-space: nowrap;
    font-size: 58px; font-weight: 800; color: var(--navy); line-height: 1;
  }
  .tagline-highlight {
    display: inline-flex; align-items: center; height: 68px;
    margin-left: 14px; padding: 0 10px;
    background: var(--green); color: #fff;
  }

  .phone-box {
    position: absolute; left: 207px; top: 344px; width: 742px; height: 111px;
    border: 3px solid var(--navy);
    display: flex; align-items: center; padding-left: 50px; gap: 28px;
    white-space: nowrap;
  }
  .phone-icon { width: 68px; height: 66px; flex: none; }
  .phone-number {
    font-size: 52px; font-weight: 700; color: var(--navy);
    letter-spacing: 10px; line-height: 1; white-space: nowrap;
  }

  .contact {
    position: absolute; top: 518px; left: 0; height: 24px;
    display: flex; align-items: center; gap: 10px; white-space: nowrap;
    font-size: 15px; color: var(--ink); line-height: 1;
  }
  .contact svg { flex: none; }
  .contact-email { left: 41px; }
  .contact-web { left: 450px; }
  .contact-license { left: 793px; font-weight: 700; font-size: 16px; }
</style>
</head>
<body>
  <section class="sign">
    <svg class="sign-corners" viewBox="0 0 1828 914" preserveAspectRatio="none" aria-hidden="true">
      <polygon points="0,0 750,0 0,624" fill="var(--green)"/>
      <polygon points="0,0 712,0 0,594" fill="var(--black)"/>
      <polygon points="1478,914 1828,624 1828,914" fill="var(--green)"/>
      <polygon points="1520,914 1828,659 1828,914" fill="var(--black)"/>
    </svg>

    <div class="brand">
      <span class="brand-mark"></span>
      <span class="brand-name">THORNWELL</span>
      <span class="brand-sub">BUILDING COMPANY</span>
    </div>

    <h1 class="headline">BUILD</h1>
    <p class="tagline">With the <span class="tagline-highlight">T-Crew</span></p>

    <div class="phone-box">
      <svg class="phone-icon" viewBox="0 0 68 66" aria-hidden="true">
        <path d="M14 3 C8 4 1 9 1 18 C2 33 17 52 30 60 C38 65 46 65 50 60 C53 57 52 53 48 51 L40 47 C37 46 35 47 33 50 C31 52 29 52 27 50 C20 44 15 37 13 30 C12 27 14 26 16 25 C19 24 20 21 19 18 L18 7 C18 4 16 3 14 3 Z" fill="var(--navy)"/>
        <g fill="none" stroke="var(--navy)" stroke-width="2.6" stroke-linecap="round">
          <path d="M36 13 C42 14 46 19 46 25"/>
          <path d="M36 6 C47 7 53 15 53 25"/>
          <path d="M37 0 C52 2 61 12 61 24"/>
        </g>
      </svg>
      <span class="phone-number">472-318-6095</span>
    </div>

    <div class="contact contact-email">
      <svg width="26" height="20" viewBox="0 0 26 20" aria-hidden="true">
        <rect x="1" y="1" width="24" height="18" fill="none" stroke="var(--ink)" stroke-width="2"/>
        <path d="M1 1 L13 11 L25 1 M1 19 L10 9 M25 19 L16 9" fill="none" stroke="var(--ink)" stroke-width="2"/>
      </svg>
      <span>thornwellbuildingcompany@mailvistra.net</span>
    </div>

    <div class="contact contact-web">
      <svg width="24" height="24" viewBox="0 0 24 24" aria-hidden="true">
        <g fill="none" stroke="var(--ink)" stroke-width="1.6">
          <circle cx="12" cy="12" r="11"/>
          <ellipse cx="12" cy="12" rx="5" ry="11"/>
          <path d="M12 1 V23 M1 12 H23 M3 6.5 H21 M3 17.5 H21"/>
        </g>
      </svg>
      <span>thornwellbuildingcompany.com</span>
    </div>

    <div class="contact contact-license">Lic# 5386204</div>
  </section>
</body>
</html>
```